Financial Planning business needs a new Business Card design

We need a business card design for an Australian financial planning business. I am looking for a clean simple design

Target Market(s)

People aged 25-40

Industry/Entity Type

Financial Service

Contact Information for Business Card

On the front of the card we need the following information:
Name: Colin Merrow (First Name Green: #006838 and last name Grey: #414042)
Position: Financial Adviser
Qualifications: BEc(Hons), AdDipFS(FP), Dip FMBM, CFL®
Mobile: 0437 512 604
Email: colin@brightledgeplan.com.au

On the back of the card we need:
Postal address: PO BOX 5307, PERTH BC, WA 6849
Website: www.brightledgeplan.com.au
Text: AFS Licence No. 518760

The fields need to be able to be edited.

Font styles to use
Sans Serif

Requirements
Must have
• Information listed above

```html
<!DOCTYPE html>
<html lang="en">
<head>
<meta charset="utf-8">
<title>Brightledge – Business Card</title>
<link rel="stylesheet" href="https://fonts.googleapis.com/css2?family=Lato:wght@400;700;900&display=swap">
<style>
  :root {
    --green: #006838;
    --grey: #414042;
    --card-grey: #4a4a4c;
    --white: #ffffff;
    --backdrop: #e9e9ea;
  }
  * { box-sizing: border-box; margin: 0; padding: 0; }
  html, body { width: 1200px; height: 900px; overflow: hidden; }
  body {
    position: relative;
    background: var(--backdrop);
    font-family: "Lato", Arial, sans-serif;
  }
  .card {
    position: absolute;
    width: 540px;
    height: 310px;
    border-radius: 3px;
    overflow: hidden;
    box-shadow: 0 14px 30px rgba(0,0,0,.28);
  }
  /* back of card */
  .card-back {
    left: 590px; top: 150px;
    background: var(--card-grey);
    color: var(--white);
  }
  .card-back .wordmark {
    position: absolute;
    left: 0; right: 0; top: 108px;
    text-align: center;
    font-weight: 900;
    font-size: 52px;
    letter-spacing: 1px;
    color: var(--white);
  }
  .card-back .legal-line {
    position: absolute;
    left: 0; right: 0; top: 206px;
    text-align: center;
    font-size: 14px;
    letter-spacing: 1.2px;
  }
  /* front of card */
  .card-front {
    left: 70px; top: 440px;
    background: var(--white);
    z-index: 2;
  }
  .card-front .shape { position: absolute; inset: 0; }
  .card-front .wordmark {
    position: absolute;
    left: 32px; top: 38px;
    font-weight: 900;
    font-size: 46px;
    letter-spacing: 1px;
    color: var(--green);
  }
  .postal {
    position: absolute;
    left: 24px; top: 228px;
    color: var(--white);
    font-size: 13px;
    font-style: normal;
    line-height: 1.35;
    letter-spacing: .5px;
  }
  .contact {
    position: absolute;
    right: 22px; top: 198px;
    text-align: right;
    color: var(--white);
  }
  .person-name { font-size: 21px; font-weight: 400; line-height: 1.1; }
  .person-name .first { color: var(--green); }
  .role { font-size: 13px; margin-top: 1px; }
  .quals { font-size: 11px; margin-top: 1px; }
  .contact-line {
    display: flex; justify-content: flex-end; align-items: center; gap: 7px;
    margin-top: 2px;
  }
  .phone { font-size: 15px; letter-spacing: .5px; }
  .email { font-size: 13px; }
  .contact-line svg { width: 12px; height: 12px; flex: none; }
</style>
</head>
<body>

  <section class="card card-back" aria-label="Business card back">
    <div class="wordmark">BRIGHTLEDGE</div>
    <p class="legal-line">www.brightledgeplan.com.au &bull; AFS Licence No. 518760</p>
  </section>

  <section class="card card-front" aria-label="Business card front">
    <svg class="shape" viewBox="0 0 540 310" preserveAspectRatio="none" aria-hidden="true">
      <path d="M210,222 Q440,215 540,110 L540,310 L210,310 Z" fill="var(--green)"/>
      <path d="M0,150 Q250,290 540,150 L540,310 L0,310 Z" fill="var(--card-grey)"/>
    </svg>

    <div class="wordmark">BRIGHTLEDGE</div>

    <address class="postal">
      PO BOX 5307,<br>PERTH BC, WA 6849
    </address>

    <div class="contact">
      <p class="person-name"><span class="first">Colin</span> Merrow</p>
      <p class="role">Financial Adviser</p>
      <p class="quals">BEc(Hons), AdDipFS(FP), Dip FMBM, CFL®</p>
      <p class="contact-line phone">0437 512 604
        <svg viewBox="0 0 12 12" aria-hidden="true"><rect x="3" y="0.5" width="6" height="11" rx="1.2" fill="var(--green)"/><rect x="4" y="2" width="4" height="7" fill="var(--card-grey)"/></svg>
      </p>
      <p class="contact-line email">colin@brightledgeplan.com.au
        <svg viewBox="0 0 12 12" aria-hidden="true"><rect x="0.5" y="2.5" width="11" height="7" fill="var(--green)"/><path d="M0.5,2.5 L6,7 L11.5,2.5" fill="none" stroke="var(--card-grey)" stroke-width="1"/></svg>
      </p>
    </div>
  </section>

</body>
</html>
```